Business card and stationery
Clear Harbour
Project: Business card and stationery
Business card and stationery  -
Creative Brief
Simple
Name Surname
Executive Director
317 Larkmoor Lane, #03 Fenwick Plaza, Country 264519
vantolemu@mailpost.example
www.clearharbour.example.sg
info (name, address, email etc) on the card should be editable for each employee

```html
<!DOCTYPE html>
<html lang="en">
<head>
<meta charset="utf-8">
<title>Clear Harbour – Business Card</title>
<link href="https://fonts.googleapis.com/css2?family=Open+Sans:wght@400;600;700&display=swap" rel="stylesheet">
<style>
  :root {
    --page-bg: #ece9e4;
    --card-bg: #ffffff;
    --card-edge: #d9d9d9;
    --brand-blue: #1f6fd6;
    --tab-blue: #2e7be6;
    --text-dark: #333333;
    --text-mid: #555555;
    --rule: #c9c9c9;
  }
  * { box-sizing: border-box; margin: 0; padding: 0; }
  html, body { width: 1200px; height: 581px; overflow: hidden; }
  body {
    background: var(--page-bg);
    font-family: "Open Sans", Arial, sans-serif;
    position: relative;
  }
  .card {
    position: absolute;
    top: 144px;
    width: 480px;
    height: 380px;
    background: linear-gradient(180deg, #ffffff 0%, #f6f6f6 100%);
    border: 1px solid var(--card-edge);
    border-radius: 16px;
    box-shadow: 0 4px 10px rgba(0,0,0,0.12);
  }
  .card--front { left: 96px; }
  .card--back { left: 605px; }

  .card__tab {
    position: absolute;
    width: 12px;
    height: 74px;
    top: 101px;
    background: var(--tab-blue);
  }
  .card__tab--left { left: -1px; border-radius: 0 3px 3px 0; }
  .card__tab--right { right: -1px; border-radius: 3px 0 0 3px; }

  .brand {
    position: absolute;
    display: flex;
    flex-direction: column;
    align-items: center;
    gap: 12px;
  }
  .brand__dot {
    width: 46px;
    height: 46px;
    border-radius: 50%;
    background: var(--brand-blue);
  }
  .brand__name {
    font-weight: 700;
    font-size: 31px;
    color: var(--brand-blue);
    white-space: nowrap;
    letter-spacing: -0.3px;
  }
  .card--front .brand { left: 26px; width: 260px; top: 92px; }
  .card--back .brand { left: 0; width: 100%; top: 92px; }

  .details {
    position: absolute;
    left: 276px;
    top: 70px;
    width: 190px;
    padding-left: 16px;
    border-left: 1px solid var(--rule);
    min-height: 230px;
  }
  .details__name {
    font-weight: 600;
    font-size: 19px;
    color: var(--brand-blue);
    line-height: 1.1;
  }
  .details__role {
    font-weight: 700;
    font-size: 11.5px;
    color: var(--text-dark);
    margin-top: 3px;
  }
  .details__address {
    font-size: 11.5px;
    color: var(--text-mid);
    line-height: 1.45;
    margin-top: 30px;
  }
  .contacts {
    list-style: none;
    margin-top: 34px;
  }
  .contacts li {
    display: flex;
    align-items: center;
    gap: 7px;
    font-size: 11px;
    color: var(--text-mid);
    line-height: 1.75;
    white-space: nowrap;
  }
  .contacts svg { width: 12px; height: 12px; flex: none; }

  .card__web {
    position: absolute;
    bottom: 48px;
    left: 0;
    width: 100%;
    text-align: center;
    font-weight: 600;
    font-size: 14px;
    color: var(--text-dark);
  }
</style>
</head>
<body>
  <section class="card card--front">
    <span class="card__tab card__tab--left"></span>
    <span class="card__tab card__tab--right"></span>

    <div class="brand">
      <span class="brand__dot"></span>
      <span class="brand__name">Clear Harbour</span>
    </div>

    <div class="details">
      <p class="details__name">Name Surname</p>
      <p class="details__role">Executive Director</p>
      <p class="details__address">317 Larkmoor Lane,<br>#03 Fenwick Plaza,<br>Country 264519</p>
      <ul class="contacts">
        <li>
          <svg viewBox="0 0 12 12"><path d="M3 1l2 2.5-1.2 1.3a6 6 0 0 0 3.4 3.4L8.5 7 11 9l-1.3 1.8C5.5 10.5 1.5 6.5 1.2 2.3z" fill="var(--brand-blue)"/></svg>
          +65 6120 4417
        </li>
        <li>
          <svg viewBox="0 0 12 12"><rect x="3" y="0.5" width="6" height="11" rx="1.2" fill="var(--brand-blue)"/><rect x="4.2" y="2" width="3.6" height="6.5" fill="#fff"/></svg>
          +65 9384 2206
        </li>
        <li>
          <svg viewBox="0 0 12 12"><circle cx="6" cy="6" r="5.5" fill="var(--brand-blue)"/><path d="M3 4h6v4H3z M3 4l3 2.2L9 4" fill="none" stroke="#fff" stroke-width="0.9"/></svg>
          vantolemu@mailpost.example
        </li>
        <li>
          <svg viewBox="0 0 12 12"><circle cx="6" cy="6" r="5.5" fill="var(--brand-blue)"/><path d="M1.5 6h9M6 1.5c-2 2.5-2 6.5 0 9M6 1.5c2 2.5 2 6.5 0 9" fill="none" stroke="#fff" stroke-width="0.8"/></svg>
          www.clearharbour.example.sg
        </li>
      </ul>
    </div>
  </section>

  <section class="card card--back">
    <div class="brand">
      <span class="brand__dot"></span>
      <span class="brand__name">Clear Harbour</span>
    </div>
    <p class="card__web">www.clearharbour.example.sg</p>
  </section>
</body>
</html>
```